Book on a defense of Christianity needs a cover design.

I need a cover for a book providing a fair and balanced factually supported logical defense of three sources related to Christian beliefs: Old Testament, New Testament, and Book of Mormon. It is written in easy to follow language in a father-to-son question and answer format. There are extensive footnotes that allow the reader to go to the source and research all things stated in the book. Both the positive evidence and the negative evidence is presented in respectful language. The final point is a proof of the validity of Christian basic beliefs. The title of the book is: Listen Well, Young One: When Doubt Comes Knocking. Letters from a father to his son regarding an evidence based logical approach to combat the secular attacks on Christianity.
Target Market(s)
General public
Industry/Entity Type
Defense
Requirements
Nice to have
- Color. Attention grabbing design. Can be abstract.

```html
<!DOCTYPE html>
<html lang="en">
<head>
<meta charset="utf-8">
<title>Listen Well, Young One: When Doubt Comes Knocking — Cover Spread</title>
<link href="https://fonts.googleapis.com/css2?family=Cinzel:wght@400;600;700&family=Tinos:wght@400&display=swap" rel="stylesheet">
<style>
  :root {
    --page: #ffffff;
    --parchment-light: #dcb86c;
    --parchment-mid: #c2954a;
    --parchment-dark: #8a5f26;
    --band-blue: #2c4f9c;
    --band-deep: #16316d;
    --band-night: #1b2232;
    --title-red: #7e1b12;
    --title-navy: #14202d;
    --ink: #2a1d0f;
    --seal-red: #b3140f;
    --seal-dark: #6e0907;
    --strip-blue: #2747a3;
    --robe-light: #caa06a;
    --robe-dark: #8d6236;
    --book-cream: #ecd3a2;
  }
  * { margin: 0; padding: 0; box-sizing: border-box; }
  html, body { width: 1200px; height: 1200px; overflow: hidden; background: var(--page); }
  body { position: relative; font-family: "Tinos", "Times New Roman", serif; }

  .spread { position: absolute; left: 14px; top: 158px; width: 1171px; height: 866px;
    background: radial-gradient(ellipse at 35% 40%, var(--parchment-light) 0%, var(--parchment-mid) 60%, var(--parchment-dark) 100%); overflow: hidden; }
  .front-panel { position: absolute; left: 602px; top: 0; width: 569px; height: 866px;
    background: radial-gradient(ellipse at 55% 35%, var(--parchment-light) 0%, var(--parchment-mid) 65%, var(--parchment-dark) 100%);
    box-shadow: -4px 0 8px rgba(60,35,10,.35); }

  .band { position: absolute; top: 0; height: 82px; border-bottom: 2px solid var(--title-navy);
    display: flex; align-items: flex-end; justify-content: center; padding-bottom: 10px;
    font-family: "Cinzel", serif; color: #fff; font-weight: 600; white-space: nowrap; }
  .band--back { left: 0; width: 602px; font-size: 25px; letter-spacing: .5px;
    background: linear-gradient(180deg, var(--band-blue), var(--band-deep)); }
  .band--front { left: 602px; width: 569px; font-size: 31px; letter-spacing: .5px;
    background: linear-gradient(90deg, var(--band-blue) 0%, var(--band-deep) 70%, var(--band-night) 100%); }

  .title { position: absolute; font-family: "Cinzel", serif; font-weight: 700; }
  .title .red { fill: var(--title-red); }
  .title .navy { fill: var(--title-navy); }

  .seal { position: absolute; border-radius: 50%;
    background: radial-gradient(circle at 40% 38%, var(--seal-red) 0%, #8f0f0b 65%, var(--seal-dark) 100%);
    box-shadow: 2px 3px 6px rgba(40,10,5,.5); }

  .blurb { position: absolute; left: 34px; top: 282px; width: 520px; color: var(--ink);
    font-size: 14.4px; line-height: 16.8px; text-align: justify; hyphens: auto; }
  .blurb p { margin-bottom: 16.8px; }
  .blurb p:last-of-type { text-align-last: center; }
  .author { position: absolute; font-family: "Cinzel", serif; font-weight: 700; color: var(--title-navy); white-space: nowrap; }
  .author--back { left: 0; width: 602px; top: 624px; text-align: center; font-size: 16px; letter-spacing: .5px; }
  .author--front { left: 602px; width: 569px; top: 818px; text-align: center; font-size: 23px; letter-spacing: 1px; }

  .spine { position: absolute; left: 578px; top: 126px; height: 700px; width: 24px;
    writing-mode: vertical-rl; font-family: "Tinos", serif; font-size: 14px; letter-spacing: 1px; white-space: nowrap; }
  .spine__title { color: var(--title-red); margin-bottom: 38px; }
  .spine__author { color: var(--title-navy); }

  .figure-art { position: absolute; left: 640px; top: 420px; width: 531px; height: 446px;
    background: radial-gradient(ellipse at 60% 55%, var(--robe-light) 0%, #b58650 50%, var(--robe-dark) 100%);
    opacity: .85; border-radius: 40% 20% 0 0; }
  .book-art { position: absolute; left: 832px; top: 580px; width: 216px; height: 220px;
    background: linear-gradient(160deg, var(--book-cream), #c9a46a); transform: rotate(-8deg); border-radius: 4px;
    box-shadow: 2px 4px 8px rgba(70,40,10,.4); }

  .strip { position: absolute; left: 602px; top: 0; width: 569px; height: 866px; }
  .letter { position: absolute; left: 610px; top: 410px; width: 356px; color: #fff;
    font-size: 11px; line-height: 15.6px; }
  .letter p { margin-bottom: 7px; }
</style>
</head>
<body>
  <div class="spread">
    <section class="back-panel">
      <div class="band band--back">LISTEN WELL, YOUNG ONE:</div>

      <svg class="title" style="left:0;top:82px" width="602" height="170" viewBox="0 0 602 170">
        <text class="red" x="218" y="60" font-size="24" textLength="72" lengthAdjust="spacingAndGlyphs">WHEN</text>
        <text class="red" x="300" y="60" font-size="64" textLength="270" lengthAdjust="spacingAndGlyphs">DOUBT</text>
        <text class="red" x="270" y="116" font-size="64" textLength="300" lengthAdjust="spacingAndGlyphs">COMES</text>
        <text class="navy" x="206" y="158" font-size="42" textLength="364" lengthAdjust="spacingAndGlyphs">KNOCKING</text>
      </svg>
      <div class="seal" role="img" aria-label="Red wax seal stamped with a dove" style="left:126px;top:130px;width:76px;height:76px"></div>

      <div class="blurb">
        <p>Our Christian youth, their parents, and the faithful are being bombarded with secular thinking and ideals. There are loud voices designed to not only discourage active participation in religious practice but to ridicule it. These voices are undercurrents that are receiving increased influence in the world society.</p>
        <p>We arm our children by teaching them the gospel. We teach them to pray. We teach them to feel the Spirit. We encourage our children to read and ponder the scriptures and to build their own testimonies. We encourage church attendance and other wholesome activities to that they will keep the goals they have set. At the same time, many of the world’s authoritative voices are shouting opposite principles, even ridiculing and attacking.</p>
        <p>This book openly acknowledges strengths and weaknesses of both skeptics and defenders, weighing each side in consideration of rational, data focused, conclusions that can enable both sides in a civil discussion.</p>
        <p>Here are specific questions and answers between son and father that will help protect a fragile testimony by arming with concrete evidence and reason that strongly support a rationally focused religious position.</p>
      </div>
      <div class="author author--back">DANIEL R. WHITCOMBE, PHD</div>
    </section>

    <div class="spine">
      <span class="spine__title">LISTEN WELL, YOUNG ONE&nbsp;&nbsp;WHEN DOUBT COMES KNOCKING</span>
      <span class="spine__author">DANIEL R. WHITCOMBE, PHD</span>
    </div>

    <section class="front-panel"></section>
    <div class="band band--front">LISTEN WELL, YOUNG ONE:</div>

    <div class="figure-art" role="img" aria-label="Painted robed figure in warm earth tones"></div>
    <div class="book-art" role="img" aria-label="Open ancient book with Greek and Latin script"></div>

    <svg class="strip" viewBox="0 0 569 866" aria-hidden="true">
      <polygon fill="var(--strip-blue)" points="0,412 60,404 110,398 150,392 200,386 240,378 300,372 340,366 382,356 400,380 395,420 380,470 360,520 300,538 250,548 200,566 150,588 100,608 60,628 0,650"/>
    </svg>

    <div class="letter">
      <p>Dear Dad: The other day in class, one professor said, “Religion . . . relies on the gullibility of its clients, who have been educated to believe without evidence and without explanation.” The basic assumption is that Christianity has no concrete, scientific “proof”, but is based only on blind and ignorant faith. I have to admit, I’m being shaken by this stuff. Is there any physical evidence at all that Jesus lived and that the scriptures are true?</p>
      <p>Dear Son: Clearly a testimony of spiritual things are spiritual in nature. But while you are in this struggle, let me assure you there is compelling physical (empirical) evidence and strong logic supporting Christian concepts.<br>Let us get started.</p>
    </div>

    <div class="seal" role="img" aria-label="Red wax seal stamped with a dove" style="left:966px;top:440px;width:100px;height:100px"></div>

    <svg class="title" style="left:602px;top:82px" width="569" height="280" viewBox="0 0 569 280">
      <text class="red" x="46" y="80" font-size="46" textLength="150" lengthAdjust="spacingAndGlyphs">WHEN</text>
      <text class="red" x="208" y="96" font-size="124" textLength="326" lengthAdjust="spacingAndGlyphs">DOUBT</text>
      <text class="red" x="44" y="196" font-size="124" textLength="488" lengthAdjust="spacingAndGlyphs">COMES</text>
      <text class="navy" x="42" y="268" font-size="70" textLength="494" lengthAdjust="spacingAndGlyphs">KNOCKING</text>
    </svg>

    <div class="author author--front">DANIEL R. WHITCOMBE, PHD</div>
  </div>
</body>
</html>
```